Business card design for a debt inventory management software company

We need a business card design to help us move into the next phase of our business. We developed an innovative solution to help companies collect their bad debts. We are moving into a new era and branching out into new industries. We are open to design ideas but would like that they have a similar feel/look to our website and include our logo. https://www.lumoryx.com

Target Market(s)

Finance Industry, Telecom Industry, Utility Industry, Healthcare Industry, Insurance Industry

Industry/Entity Type

Software

Contact Information for Business Card

Include Name, Title, Phone, Email, website, address, and logo

Font styles to use
Sans Serif

Colors

Designer to choose colors to be used in the design.

Requirements
Must have
• A similar look and feel to our website. https://www.lumoryx.com

```html
<!DOCTYPE html>
<html lang="en">
<head>
<meta charset="utf-8">
<title>Lumoryx Software – Business Cards</title>
<link href="https://fonts.googleapis.com/css2?family=Lato:wght@300;400;700&display=swap" rel="stylesheet">
<style>
  :root{
    --stage:#2b2e33;
    --card-white:#ffffff;
    --brand-blue:#23399a;
    --brand-blue-dark:#1c2f82;
    --slate:#5a5c60;
    --slate-dark:#45474b;
    --ink:#2c2c2c;
    --ink-soft:#3a3a3a;
    --accent-red:#c8262d;
  }
  *{margin:0;padding:0;box-sizing:border-box}
  html,body{width:1200px;height:900px;overflow:hidden;background:var(--stage);font-family:"Lato",Arial,sans-serif}
  .stage{position:relative;width:1200px;height:900px}
  .card{position:absolute;width:520px;height:297px;border-radius:22px;overflow:hidden;background:var(--card-white);box-shadow:0 14px 30px rgba(0,0,0,.45)}
  .card svg.bg{position:absolute;inset:0;width:100%;height:100%}

  /* Front */
  .card--front{left:90px;top:480px}
  .person{position:absolute;left:34px;top:30px}
  .person__name{font-size:24px;font-weight:700;letter-spacing:.5px;color:var(--brand-blue)}
  .person__name span{color:var(--ink-soft)}
  .person__title{font-size:15px;font-weight:700;color:var(--ink-soft);margin-top:2px}
  .contact{list-style:none;position:absolute;left:34px;top:102px}
  .contact li{display:flex;align-items:center;gap:10px;font-size:15px;color:var(--ink);height:24px}
  .contact svg{width:15px;height:15px;fill:var(--brand-blue)}
  .address{position:absolute;left:34px;bottom:26px;color:#fff;font-size:15px;line-height:21px;font-weight:400}
  .front-brand{position:absolute;right:40px;top:112px;display:flex;align-items:center;gap:12px}
  .front-brand__mark{width:40px;height:40px;background:var(--brand-blue)}
  .front-brand__name{font-size:30px;font-weight:300;color:var(--brand-blue)}

  /* Back */
  .card--back{left:590px;top:140px}
  .back-brand{position:absolute;left:44px;top:122px;display:flex;align-items:center;gap:14px}
  .back-brand__mark{width:30px;height:30px;background:var(--brand-blue)}
  .back-brand__name{font-size:38px;font-weight:300;color:var(--brand-blue);letter-spacing:.3px}
  .back-brand__name span{color:var(--slate)}
</style>
</head>
<body>
<main class="stage">

  <section class="card card--front" aria-label="Business card front">
    <svg class="bg" viewBox="0 0 520 297" preserveAspectRatio="none" aria-hidden="true">
      <polygon points="0,205 300,205 345,297 0,297" fill="var(--brand-blue)"/>
      <polygon points="345,297 300,205 520,205 520,297" fill="var(--slate)"/>
    </svg>
    <div class="person">
      <h1 class="person__name">MARCUS <span>HALE</span></h1>
      <p class="person__title">Director</p>
    </div>
    <ul class="contact">
      <li><svg viewBox="0 0 24 24"><path d="M6.6 10.8a15 15 0 0 0 6.6 6.6l2.2-2.2c.3-.3.7-.4 1-.2 1.1.4 2.3.6 3.6.6.6 0 1 .4 1 1V20c0 .6-.4 1-1 1A17 17 0 0 1 3 4c0-.6.4-1 1-1h3.5c.6 0 1 .4 1 1 0 1.3.2 2.5.6 3.6.1.3 0 .7-.2 1z"/></svg>555.014.0290</li>
      <li><svg viewBox="0 0 24 24"><path d="M2 5h20v14H2z" fill="none"/><path d="M2 5h20v14H2V5zm2 2v.5l8 5 8-5V7H4zm0 2.8V17h16V9.8l-8 5z"/></svg>info@lumoryx.com</li>
      <li><svg viewBox="0 0 24 24"><path d="M12 2a10 10 0 1 0 0 20 10 10 0 0 0 0-20zm6.9 6h-3a15 15 0 0 0-1.3-3.9A8 8 0 0 1 18.9 8zM12 4c.9 1.2 1.6 2.5 2 4h-4c.4-1.5 1.1-2.8 2-4zM4.3 14a8 8 0 0 1 0-4h3.4a16 16 0 0 0 0 4zm.8 2h3a15 15 0 0 0 1.3 3.9A8 8 0 0 1 5.1 16zM8 8H5.1a8 8 0 0 1 4.3-3.9C8.8 5.3 8.3 6.6 8 8zm4 12c-.9-1.2-1.6-2.5-2-4h4c-.4 1.5-1.1 2.8-2 4zm2.3-6H9.7a14 14 0 0 1 0-4h4.6a14 14 0 0 1 0 4zm.3 5.9c.6-1.2 1.1-2.5 1.3-3.9h3a8 8 0 0 1-4.3 3.9zm1.7-5.9a16 16 0 0 0 0-4h3.4a8 8 0 0 1 0 4z"/></svg>www.lumoryx.com</li>
    </ul>
    <div class="front-brand">
      <div class="front-brand__mark"></div>
      <div class="front-brand__name">Lumoryx</div>
    </div>
    <address class="address" style="font-style:normal">420 Harbor Crest Avenue<br>Suite 210, Brookfield, Ohio 44000</address>
  </section>

  <section class="card card--back" aria-label="Business card back">
    <svg class="bg" viewBox="0 0 520 297" preserveAspectRatio="none" aria-hidden="true">
      <rect x="0" y="0" width="520" height="82" fill="var(--slate-dark)"/>
      <rect x="0" y="212" width="520" height="85" fill="var(--brand-blue)"/>
      <circle cx="260" cy="82" r="9" fill="var(--stage)"/>
      <circle cx="260" cy="212" r="9" fill="var(--stage)"/>
    </svg>
    <div class="back-brand">
      <div class="back-brand__mark"></div>
      <div class="back-brand__name">Lumoryx <span>Software</span></div>
    </div>
  </section>

</main>
</body>
</html>
```